Telecommunication company needs a car wrap design for 3 vans

We are a telecommunication company called "Brivon" based in Australia's capital city Canberra.
We have the logo, colour scheme, website (www.brivon.com.au) and complete brand guidelines created. Now we need a design for two KD Haulmarks LWB (one in white and one in grey colour) and one Morvane Kestrel LWB (also in white colour).
We would like a modern design which stands out as colours are very neutral and will look uniform on all cars. We preffer not to have fully wrapped car design but open for suggestions.
Please referr to attachments.

List of services:
- antenna and satellite
- tv wall mounting
- phone and data
- home theatre
- cabling contractor

Dear Participants, thank you for your designs, some of them were better than others. What we really liked was your creativity, however most of the designs would not be aplicable on the grey colour vehicle as the colours would not simply play together. Also many of the designs were missing services as a vital part of van signage. Please bear this in your mind. We are starting a new round of designs and will be very happy if you all will participate again and bring your ideas. Good luck to everyone. Kind Regards,

• Logo on the bonet

Sides and rear must have logo, website, phone number, sevices

List of services:
- antenna and satellite
- tv wall mounting
- phone and data
- home theatre
- cabling contractor
• social media icons

```html
<!DOCTYPE html>
<html lang="en">
<head>
<meta charset="utf-8">
<title>Brivon van wrap concepts</title>
<link rel="stylesheet" href="https://fonts.googleapis.com/css2?family=Catamaran:wght@500;600;700&display=swap">
<style>
  :root {
    --canvas: #ffffff;
    --navy: #323a4a;
    --charcoal: #3b4049;
    --charcoal-deep: #2f3237;
    --stone: #e3e3df;
    --stone-grey: #cfcfca;
    --glass: #cdcfd1;
    --tyre: #33363b;
    --rim: #c9cbcd;
    --hub: #5a5e64;
    --paper: #ececea;
  }
  html, body {
    margin: 0;
    width: 1200px;
    height: 636px;
    overflow: hidden;
    background: var(--canvas);
  }
  .fleet { display: block; width: 1200px; height: 636px; }
  .brand-text { font-family: "Catamaran", sans-serif; }

  .van--white { --base: var(--charcoal-deep); --panel: var(--stone); --ink: var(--navy); }
  .van--grey  { --base: var(--stone-grey); --panel: var(--charcoal); --ink: var(--paper); }

  .body-base  { fill: var(--base); }
  .wrap-panel { fill: var(--panel); }
  .window     { fill: var(--glass); stroke: #2a2c30; stroke-width: 2; }
  .panel-line { fill: none; stroke: rgba(0,0,0,.28); stroke-width: 1; }
  .tyre { fill: var(--tyre); }
  .rim  { fill: var(--rim); }
  .hub  { fill: var(--hub); }
  .lamp { fill: #b23a2e; }
  .shadow { fill: rgba(0,0,0,.12); }

  .wordmark { font-weight: 600; font-size: 44px; fill: var(--ink); text-anchor: middle; }
  .web      { font-weight: 600; font-size: 11px; fill: var(--ink); text-anchor: middle; }
  .phone    { font-weight: 700; font-size: 13px; fill: var(--ink); text-anchor: middle; }
  .service  { font-weight: 600; font-size: 7.2px; fill: var(--ink); }
  .mark-dot { fill: none; stroke: var(--ink); stroke-width: 5; }
  .bullet   { fill: none; stroke: var(--ink); stroke-width: 1; }
  .social   { fill: var(--ink); }
</style>
</head>
<body>
<svg class="fleet" viewBox="0 0 1200 636" xmlns="http://www.w3.org/2000/svg">
  <defs>
    <clipPath id="body-clip">
      <path d="M12,190 L10,140 Q14,118 60,102 L120,62 Q160,26 200,18 L500,12 Q518,12 520,24 L528,170 Q530,190 515,192 Z"/>
    </clipPath>
    <g id="van-art">
      <ellipse class="shadow" cx="270" cy="222" rx="265" ry="6"/>
      <path class="body-base" d="M12,190 L10,140 Q14,118 60,102 L120,62 Q160,26 200,18 L500,12 Q518,12 520,24 L528,170 Q530,190 515,192 Z"/>
      <g clip-path="url(#body-clip)">
        <path class="wrap-panel" d="M0,0 H506 Q488,128 372,141 H0 Z"/>
      </g>
      <path class="window" d="M140,78 L148,40 Q160,20 180,18 L236,16 L236,80 Z"/>
      <path class="panel-line" d="M128,80 L128,196 M252,18 L252,196 M252,14 L500,12 M258,20 L490,18 L490,98 M258,20 L258,110"/>
      <rect class="lamp" x="515" y="96" width="8" height="30" rx="2"/>
      <g><circle class="tyre" cx="94" cy="184" r="37"/><circle class="rim" cx="94" cy="184" r="24"/><circle class="hub" cx="94" cy="184" r="6"/></g>
      <g><circle class="tyre" cx="434" cy="184" r="37"/><circle class="rim" cx="434" cy="184" r="24"/><circle class="hub" cx="434" cy="184" r="6"/></g>
    </g>
  </defs>

  <!-- Van 1: white, front left -->
  <g class="van van--white" transform="translate(20,26)">
    <use href="#van-art"/>
    <g class="brand-text">
      <circle class="mark-dot" cx="356" cy="44" r="24"/>
      <text class="wordmark" x="356" y="114">brivon</text>
      <text class="web" x="356" y="136">brivon.com.au</text>
      <text class="phone" x="183" y="136">1300 555 214</text>
      <g class="socials"><circle class="social" cx="262" cy="22" r="5"/><circle class="social" cx="276" cy="22" r="5"/><circle class="social" cx="290" cy="22" r="5"/></g>
      <g class="services">
        <circle class="bullet" cx="412" cy="26" r="2.6"/><text class="service" x="418" y="28.5">Antenna &amp; Satellite</text>
        <circle class="bullet" cx="412" cy="35" r="2.6"/><text class="service" x="418" y="37.5">TV wall mounting</text>
        <circle class="bullet" cx="412" cy="44" r="2.6"/><text class="service" x="418" y="46.5">Phone &amp; Data</text>
        <circle class="bullet" cx="412" cy="53" r="2.6"/><text class="service" x="418" y="55.5">Home Theatre</text>
        <circle class="bullet" cx="412" cy="62" r="2.6"/><text class="service" x="418" y="64.5">Cabling contractor</text>
      </g>
    </g>
  </g>

  <!-- Van 2: grey, front left -->
  <g class="van van--grey" transform="translate(647,38)">
    <use href="#van-art"/>
    <g class="brand-text">
      <circle class="mark-dot" cx="356" cy="44" r="24"/>
      <text class="wordmark" x="356" y="114">brivon</text>
      <text class="web" x="356" y="136">brivon.com.au</text>
      <text class="phone" x="183" y="136">1300 555 214</text>
      <g class="socials"><circle class="social" cx="262" cy="22" r="5"/><circle class="social" cx="276" cy="22" r="5"/><circle class="social" cx="290" cy="22" r="5"/></g>
      <g class="services">
        <circle class="bullet" cx="412" cy="26" r="2.6"/><text class="service" x="418" y="28.5">Antenna &amp; Satellite</text>
        <circle class="bullet" cx="412" cy="35" r="2.6"/><text class="service" x="418" y="37.5">TV wall mounting</text>
        <circle class="bullet" cx="412" cy="44" r="2.6"/><text class="service" x="418" y="46.5">Phone &amp; Data</text>
        <circle class="bullet" cx="412" cy="53" r="2.6"/><text class="service" x="418" y="55.5">Home Theatre</text>
        <circle class="bullet" cx="412" cy="62" r="2.6"/><text class="service" x="418" y="64.5">Cabling contractor</text>
      </g>
    </g>
  </g>

  <!-- Van 3: white, front right -->
  <g class="van van--white" transform="translate(26,380)">
    <use href="#van-art" transform="translate(540,0) scale(-1,1)"/>
    <g class="brand-text">
      <circle class="mark-dot" cx="184" cy="44" r="24"/>
      <text class="wordmark" x="184" y="114">brivon</text>
      <text class="web" x="184" y="136">brivon.com.au</text>
      <text class="phone" x="357" y="136">1300 555 214</text>
      <g class="socials"><circle class="social" cx="250" cy="22" r="5"/><circle class="social" cx="264" cy="22" r="5"/><circle class="social" cx="278" cy="22" r="5"/></g>
      <g class="services">
        <circle class="bullet" cx="64" cy="26" r="2.6"/><text class="service" x="70" y="28.5">Antenna &amp; Satellite</text>
        <circle class="bullet" cx="64" cy="35" r="2.6"/><text class="service" x="70" y="37.5">TV wall mounting</text>
        <circle class="bullet" cx="64" cy="44" r="2.6"/><text class="service" x="70" y="46.5">Phone &amp; Data</text>
        <circle class="bullet" cx="64" cy="53" r="2.6"/><text class="service" x="70" y="55.5">Home Theatre</text>
        <circle class="bullet" cx="64" cy="62" r="2.6"/><text class="service" x="70" y="64.5">Cabling contractor</text>
      </g>
    </g>
  </g>

  <!-- Van 4: grey, front right -->
  <g class="van van--grey" transform="translate(654,371)">
    <use href="#van-art" transform="translate(540,0) scale(-1,1)"/>
    <g class="brand-text">
      <circle class="mark-dot" cx="184" cy="44" r="24"/>
      <text class="wordmark" x="184" y="114">brivon</text>
      <text class="web" x="184" y="136">brivon.com.au</text>
      <text class="phone" x="357" y="136">1300 555 214</text>
      <g class="socials"><circle class="social" cx="250" cy="22" r="5"/><circle class="social" cx="264" cy="22" r="5"/><circle class="social" cx="278" cy="22" r="5"/></g>
      <g class="services">
        <circle class="bullet" cx="64" cy="26" r="2.6"/><text class="service" x="70" y="28.5">Antenna &amp; Satellite</text>
        <circle class="bullet" cx="64" cy="35" r="2.6"/><text class="service" x="70" y="37.5">TV wall mounting</text>
        <circle class="bullet" cx="64" cy="44" r="2.6"/><text class="service" x="70" y="46.5">Phone &amp; Data</text>
        <circle class="bullet" cx="64" cy="53" r="2.6"/><text class="service" x="70" y="55.5">Home Theatre</text>
        <circle class="bullet" cx="64" cy="62" r="2.6"/><text class="service" x="70" y="64.5">Cabling contractor</text>
      </g>
    </g>
  </g>
</svg>
</body>
</html>
```